International Dating Site for modern people

We need a site design for a brand new dating site. Feel free to express your ideas and creativity. The final design should be creative and positive feeling, warm.

major elements:
- main page
- login/logout (form)
- profile editing (form)
- profile page with pictures
- search page and results page (form, table)
- a message box or the header in the main page with the following theme, feeling:
winter, spring, summer, autumn, christmas, easter, new year
- blog subpage (title, content)
- menu (login/blog/search/profile/logout)
- footer (impressum, faq, contact, privacy policy)

Target Market(s)

people between 21 and 45

Industry/Entity Type

Social

Number of Pages Required

4 page

Font styles to use
Sans Serif

Requirements
Must have
• happy, positive, warm look and feel and responsive design (plan to target different devices, the final and coded version will be responsive but please think of it when you design elements)
Nice to have
• creative

```html
<!DOCTYPE html>
<html lang="en">
<head>
<meta charset="utf-8">
<title>WarmLink – Meet New People Online</title>
<link rel="stylesheet" href="https://fonts.googleapis.com/css2?family=Roboto:wght@400;500;700&family=Open+Sans:wght@400;600&display=swap">
<style>
  :root {
    --ink: #1b1d1f;
    --night: #121416;
    --panel: #151311;
    --card-bar: #0c0c0c;
    --orange: #e8760c;
    --blue: #1a96d8;
    --white: #ffffff;
    --text: #333333;
    --muted: #777777;
    --line: #e2e2e2;
    --field: #2a2d30;
  }
  * { box-sizing: border-box; margin: 0; padding: 0; }
  html, body { width: 878px; height: 1200px; overflow: hidden; }
  body { position: relative; background: var(--white); font-family: "Open Sans", Arial, sans-serif; color: var(--text); }
  .abs { position: absolute; }

  /* Header */
  .site-header { left: 0; top: 0; width: 878px; height: 67px; background: var(--ink); }
  .brand { left: 80px; top: 20px; font-family: "Roboto", Arial, sans-serif; font-weight: 500; font-size: 19px; color: var(--white); letter-spacing: .3px; }
  .main-nav { right: 82px; top: 28px; display: flex; gap: 0; }
  .main-nav a { font-family: "Roboto", Arial, sans-serif; font-size: 9px; font-weight: 500; color: var(--white); text-decoration: none; margin-left: 35px; text-transform: uppercase; }
  .main-nav a.active { color: var(--orange); }

  /* Hero */
  .hero { left: 0; top: 67px; width: 878px; height: 386px;
    background: linear-gradient(100deg, #f3d7a6 0%, #eaa56c 22%, #c97b5a 40%, #8a6a6a 58%, #6f7784 78%, #8d95a1 100%); }
  .hero-fade { left: 0; top: 67px; width: 878px; height: 386px;
    background: linear-gradient(180deg, rgba(250,235,205,.55) 0%, rgba(250,220,180,.1) 45%, rgba(200,140,100,.25) 100%); }
  .hero-line { left: 0; top: 451px; width: 878px; height: 2px; background: var(--orange); }
  .hero-title { left: 81px; top: 222px; font-family: "Roboto", Arial, sans-serif; font-weight: 700; font-size: 22px; color: #1a1a1a; }
  .hero-text { left: 80px; top: 255px; width: 330px; font-size: 12px; line-height: 19px; color: #2a2a2a; }
  .dots { left: 81px; top: 303px; display: flex; gap: 7px; }
  .dots span { width: 7px; height: 7px; border-radius: 50%; background: #9a9a9a; }
  .dots span.on { background: var(--blue); }

  /* Tabs and profiles */
  .tabs { left: 81px; top: 396px; display: flex; gap: 1px; }
  .tab { width: 123px; height: 30px; background: #0c0c0c; color: var(--white); font-family: "Roboto", Arial, sans-serif; font-size: 11px; display: flex; align-items: center; justify-content: center; position: relative; }
  .tab.active { background: var(--orange); }
  .tab.active::after { content: ""; position: absolute; left: 56px; bottom: -6px; border: 6px solid transparent; border-bottom: 0; border-top-color: var(--orange); }
  .profiles-panel { left: 54px; top: 426px; width: 750px; height: 216px; background: var(--panel); }
  .profile-card { top: 453px; width: 165px; height: 166px; }
  .profile-photo { width: 165px; height: 123px; }
  .profile-bar { height: 43px; background: var(--card-bar); display: flex; align-items: center; justify-content: space-between; padding: 0 9px 0 14px; }
  .profile-name { font-family: "Roboto", Arial, sans-serif; font-size: 9px; color: var(--white); text-transform: uppercase; }
  .go { width: 27px; height: 27px; }

  /* Steps */
  .steps-title { left: 0; top: 690px; width: 878px; text-align: center; font-family: "Roboto", Arial, sans-serif; font-size: 19px; color: #222; }
  .step { top: 749px; width: 220px; }
  .step-head { display: flex; align-items: center; gap: 9px; }
  .step-icon { width: 31px; height: 31px; }
  .step-name { font-family: "Roboto", Arial, sans-serif; font-size: 12px; color: #222; text-transform: uppercase; }
  .step-text { margin-top: 9px; font-size: 8px; line-height: 19px; color: var(--muted); }
  .divider { top: 747px; width: 1px; height: 96px; background: var(--line); }

  /* Subscribe */
  .subscribe { left: 0; top: 892px; width: 878px; height: 221px; background: var(--night); }
  .subscribe-title { left: 0; top: 924px; width: 878px; text-align: center; font-family: "Roboto", Arial, sans-serif; font-size: 24px; color: var(--white); }
  .subscribe-text { left: 95px; top: 968px; width: 688px; text-align: center; font-size: 8px; line-height: 19px; color: #dddddd; }
  .email-field { left: 229px; top: 1024px; width: 359px; height: 48px; background: var(--field); color: #e0e0e0; font-size: 9px; padding-left: 18px; display: flex; align-items: center; }
  .email-btn { left: 588px; top: 1024px; width: 63px; height: 48px; background: var(--orange); display: flex; align-items: center; justify-content: center; }

  /* Footer */
  .site-footer { left: 0; top: 1113px; width: 878px; height: 87px; background: #0d0f11; }
  .footer-links { left: 81px; top: 1139px; font-size: 8px; color: var(--white); }
  .footer-links span { margin: 0 5px; }
  .copyright { left: 81px; top: 1160px; font-size: 8px; color: var(--white); }
  .social { top: 1146px; width: 19px; height: 19px; border-radius: 3px; }
</style>
</head>
<body>

<header class="site-header abs">
  <div class="brand abs">WarmLink</div>
  <nav class="main-nav abs">
    <a class="active" href="#">Home</a>
    <a href="#">Login</a>
    <a href="#">Blog</a>
    <a href="#">Search</a>
    <a href="#">Profile</a>
    <a href="#">Logout</a>
  </nav>
</header>

<section>
  <div class="hero abs" role="img" aria-label="Sunlit city skyline with a domed parliament building on a riverbank"></div>
  <div class="hero-fade abs"></div>
  <div class="hero-line abs"></div>
  <h1 class="hero-title abs">MEET NEW PEOPLE ONLINE</h1>
  <p class="hero-text abs">Lorem ipsum dolor sit amet, consectetuer adipiscing elit, sed diam nonummy nibh euismod tincidunt ut laoreet</p>
  <div class="dots abs"><span class="on"></span><span></span><span></span></div>
</section>

<div class="profiles-panel abs"></div>
<div class="tabs abs">
  <div class="tab active">NEW PROFILES</div>
  <div class="tab">POPULAR</div>
  <div class="tab">QUICK SEARCH</div>
</div>

<article class="profile-card abs" style="left:81px">
  <div class="profile-photo" role="img" aria-label="Man in a beanie working on a laptop in a café" style="background:linear-gradient(135deg,#6b6a66,#c9c3b8 60%,#e8e4dd)"></div>
  <div class="profile-bar"><span class="profile-name">Leo Marsh</span>
    <svg class="go" viewBox="0 0 28 28"><circle cx="14" cy="14" r="14" fill="var(--blue)"/><path d="M8 14h10M14 9l5 5-5 5" stroke="#fff" stroke-width="2.6" fill="none" stroke-linecap="round" stroke-linejoin="round"/></svg></div>
</article>
<article class="profile-card abs" style="left:265px">
  <div class="profile-photo" role="img" aria-label="Portrait of a blonde woman in a white shirt" style="background:linear-gradient(90deg,#7e9a52,#d9c6ab 45%,#e6d9c6 70%,#8aa35f)"></div>
  <div class="profile-bar"><span class="profile-name">Nora</span>
    <svg class="go" viewBox="0 0 28 28"><circle cx="14" cy="14" r="14" fill="var(--blue)"/><path d="M8 14h10M14 9l5 5-5 5" stroke="#fff" stroke-width="2.6" fill="none" stroke-linecap="round" stroke-linejoin="round"/></svg></div>
</article>
<article class="profile-card abs" style="left:449px">
  <div class="profile-photo" role="img" aria-label="Smiling woman in a striped top standing in an office" style="background:linear-gradient(90deg,#cfd6dc,#e9e6e2 45%,#b9b6b0 70%,#dfe4e8)"></div>
  <div class="profile-bar"><span class="profile-name">Ivy Carden</span>
    <svg class="go" viewBox="0 0 28 28"><circle cx="14" cy="14" r="14" fill="var(--blue)"/><path d="M8 14h10M14 9l5 5-5 5" stroke="#fff" stroke-width="2.6" fill="none" stroke-linecap="round" stroke-linejoin="round"/></svg></div>
</article>
<article class="profile-card abs" style="left:632px">
  <div class="profile-photo" role="img" aria-label="Man lying on a bed next to his beagle" style="background:linear-gradient(160deg,#e9dccb,#c79a72 45%,#8c5a4a 70%,#eeeae6)"></div>
  <div class="profile-bar"><span class="profile-name">Sam Reyes</span>
    <svg class="go" viewBox="0 0 28 28"><circle cx="14" cy="14" r="14" fill="var(--blue)"/><path d="M8 14h10M14 9l5 5-5 5" stroke="#fff" stroke-width="2.6" fill="none" stroke-linecap="round" stroke-linejoin="round"/></svg></div>
</article>

<h2 class="steps-title abs">STEPS TO FIND YOUR MATCH</h2>

<div class="step abs" style="left:81px">
  <div class="step-head">
    <svg class="step-icon" viewBox="0 0 31 31"><circle cx="15.5" cy="15.5" r="15.5" fill="var(--orange)"/><circle cx="15.5" cy="12" r="3.6" fill="#fff"/><path d="M9.5 22c0-3.6 2.7-5.6 6-5.6s6 2 6 5.6z" fill="#fff"/></svg>
    <span class="step-name">Create Profile</span>
  </div>
  <p class="step-text">Maecenas molestie dignissim lacinia. Nu llam a nulla a mi semper viverra eu ac diam. Fusce quis est eu dolor feugi at vol utpat venenatis.</p>
</div>
<div class="divider abs" style="left:315px"></div>
<div class="step abs" style="left:329px">
  <div class="step-head">
    <svg class="step-icon" viewBox="0 0 31 31"><circle cx="15.5" cy="15.5" r="15.5" fill="var(--orange)"/><path d="M15.5 23l-6.2-6.1a3.8 3.8 0 0 1 6.2-4.6 3.8 3.8 0 0 1 6.2 4.6z" fill="#fff"/></svg>
    <span class="step-name">Find Matches</span>
  </div>
  <p class="step-text">Maecenas molestie dignissim lacinia. Nu llam a nulla a mi semper viverra eu ac diam. Fusce quis est eu dolor feugi at vol utpat venenatis.</p>
</div>
<div class="divider abs" style="left:562px"></div>
<div class="step abs" style="left:577px">
  <div class="step-head">
    <svg class="step-icon" viewBox="0 0 31 31"><circle cx="15.5" cy="15.5" r="15.5" fill="var(--orange)"/><ellipse cx="13.5" cy="13.5" rx="5.5" ry="4" fill="#fff"/><path d="M10 16l-1.5 3 4-2z" fill="#fff"/><ellipse cx="18" cy="17" rx="5" ry="3.6" fill="#fff" stroke="var(--orange)" stroke-width="1"/><path d="M21 19.5l2 2.5-4-1.5z" fill="#fff"/></svg>
    <span class="step-name">Start Dating</span>
  </div>
  <p class="step-text">Maecenas molestie dignissim lacinia. Nu llam a nulla a mi semper viverra eu ac diam. Fusce quis est eu dolor feugi at vol utpat venenatis.</p>
</div>

<section>
  <div class="subscribe abs"></div>
  <h2 class="subscribe-title abs">SUBSCRIBE NOW</h2>
  <p class="subscribe-text abs">Morbi venenatis pellentesque augue. Duis porta sem neque. Pellentesque mattis massa sem, porttitor vulputate libero convallis ut. Nullam rhoncus felis ut odio venenatis iaculis. Donec rutrum velit urna. Nullam rutrum egestas enim. In hac habitae platea dictumst.</p>
  <div class="email-field abs">Email Address</div>
  <div class="email-btn abs">
    <svg width="18" height="18" viewBox="0 0 18 18"><path d="M2 9h12M9 3l6 6-6 6" stroke="#fff" stroke-width="3" fill="none" stroke-linecap="round" stroke-linejoin="round"/></svg>
  </div>
</section>

<footer>
  <div class="site-footer abs"></div>
  <div class="footer-links abs">Impressum<span>|</span>Faq<span>|</span>Contact<span>|</span>Privacy Policy</div>
  <div class="copyright abs">Copyright©2016 WarmLink. All Right Reserved.</div>
  <div class="social abs" style="left:727px;background:#3b5a9a"></div>
  <div class="social abs" style="left:752px;background:#1da1e0"></div>
  <div class="social abs" style="left:778px;background:#d9472e"></div>
</footer>

</body>
</html>
```